Business Card for Makeup Artist

I need a business card designed for my makeup and hair artistry business which is primarily events and weddings focused. The card needs to be sleek, simple, stylish and appealing to women. I would prefer a white background but open to suggestions also. I also love the marble background look. I have attached some example pics. It needs to be a double sided card with logo and/or design on one side and contact details in the centre of the card on the other side. NO LOGO ON BACK. Examples attached.

Target Market(s)

Females age 14-55

Industry/Entity Type

Business

Contact Information for Business Card

Nora Vint
Principal Makeup Artist
P: 0413 925 214
E: nora@lumirabeauty.com.au
W: www.lumirabeauty.com.au

Requirements
Should not have
• No yellow, green, red or blue in the design.

```html
<!DOCTYPE html>
<html lang="en">
<head>
<meta charset="utf-8">
<title>Lumira Makeup Artistry – Business Card</title>
<link rel="stylesheet" href="https://fonts.googleapis.com/css2?family=Montserrat:wght@300;400;700&family=Playball&display=swap">
<style>
  :root {
    --stage: #7d7d7d;
    --marble-light: #f4f4f4;
    --marble-mid: #e2e2e2;
    --marble-vein: #cfcfcf;
    --logo-grey: #5f5f5f;
    --ink: #111111;
    --accent-pink: #e8237a;
    --icon-fill: #0c0c0c;
    --icon-glyph: #ffffff;
  }
  html, body {
    margin: 0;
    padding: 0;
    width: 1200px;
    height: 960px;
    overflow: hidden;
    background: var(--stage);
  }
  .canvas {
    position: relative;
    width: 1200px;
    height: 960px;
  }
  .card {
    position: absolute;
    left: 236px;
    width: 728px;
    height: 436px;
    overflow: hidden;
  }
  .card--front { top: 28px; }
  .card--back { top: 472px; }
  .card__marble {
    position: absolute;
    inset: 0;
    background:
      linear-gradient(155deg, transparent 30%, rgba(190,190,190,0.35) 34%, transparent 38%),
      linear-gradient(160deg, transparent 58%, rgba(200,200,200,0.3) 61%, transparent 65%),
      linear-gradient(135deg, var(--marble-light) 0%, var(--marble-mid) 45%, var(--marble-light) 70%, var(--marble-mid) 100%);
  }
  .card__content {
    position: absolute;
    inset: 0;
    font-family: "Montserrat", sans-serif;
  }

  /* Front */
  .brand {
    position: absolute;
    left: 0;
    right: 0;
    top: 148px;
    text-align: center;
    color: var(--logo-grey);
  }
  .brand__name {
    margin: 0;
    font-family: "Montserrat", sans-serif;
    font-weight: 400;
    font-size: 92px;
    line-height: 1;
    letter-spacing: 4px;
  }
  .brand__tagline {
    margin: 14px 0 0;
    font-family: "Montserrat", sans-serif;
    font-weight: 300;
    font-size: 31px;
    letter-spacing: 2px;
  }

  /* Back */
  .contact {
    position: absolute;
    left: 0;
    right: 0;
    top: 0;
    text-align: center;
  }
  .contact__name {
    position: absolute;
    left: 0; right: 0;
    top: 62px;
    margin: 0;
    font-family: "Playball", cursive;
    font-weight: 400;
    font-size: 50px;
    line-height: 1;
    color: var(--ink);
  }
  .contact__role {
    position: absolute;
    left: 0; right: 0;
    top: 124px;
    margin: 0;
    font-weight: 700;
    font-size: 19px;
    letter-spacing: 0.5px;
    color: var(--accent-pink);
  }
  .contact__item {
    position: absolute;
    left: 0; right: 0;
    display: flex;
    flex-direction: column;
    align-items: center;
  }
  .contact__item--phone { top: 183px; }
  .contact__item--email { top: 255px; }
  .contact__item--web { top: 329px; }
  .contact__icon {
    width: 34px;
    height: 34px;
    display: block;
  }
  .contact__text {
    margin-top: 4px;
    font-weight: 300;
    font-size: 22px;
    letter-spacing: 0.6px;
    color: var(--ink);
  }
</style>
</head>
<body>
<main class="canvas">

  <section class="card card--front" aria-label="Card front">
    <div class="card__marble" role="img" aria-label="White marble texture background with soft grey veins"></div>
    <div class="card__content">
      <div class="brand">
        <p class="brand__name">Lumira</p>
        <p class="brand__tagline">MAKEUP ARTISTRY</p>
      </div>
    </div>
  </section>

  <section class="card card--back" aria-label="Card back">
    <div class="card__marble" role="img" aria-label="White marble texture background with soft grey veins"></div>
    <div class="card__content contact">
      <h1 class="contact__name">Nora Vint</h1>
      <p class="contact__role">PRINCIPAL MAKEUP ARTIST</p>

      <div class="contact__item contact__item--phone">
        <svg class="contact__icon" viewBox="0 0 34 34" aria-hidden="true">
          <circle cx="17" cy="17" r="17" fill="var(--icon-fill)"/>
          <path d="M12.2 9.5c.6-.4 1.3-.3 1.7.3l1.6 2.6c.3.6.2 1.2-.3 1.6l-1.2.9c.8 1.9 2.3 3.5 4.2 4.4l1-1.1c.4-.5 1.1-.6 1.6-.3l2.6 1.5c.6.3.8 1 .4 1.6l-1 1.6c-.5.8-1.5 1.2-2.4.9-4.6-1.4-8.2-5-9.5-9.6-.3-.9.1-1.9.9-2.4z" fill="var(--icon-glyph)"/>
        </svg>
        <span class="contact__text">0413 925 214</span>
      </div>

      <div class="contact__item contact__item--email">
        <svg class="contact__icon" viewBox="0 0 34 34" aria-hidden="true">
          <circle cx="17" cy="17" r="17" fill="var(--icon-fill)"/>
          <rect x="9" y="11.5" width="16" height="11" rx="1" fill="var(--icon-glyph)"/>
          <path d="M9.5 12l7.5 6 7.5-6M9.5 22l5.5-5M24.5 22l-5.5-5" fill="none" stroke="var(--icon-fill)" stroke-width="1.3"/>
        </svg>
        <span class="contact__text">nora@lumirabeauty.com.au</span>
      </div>

      <div class="contact__item contact__item--web">
        <svg class="contact__icon" viewBox="0 0 34 34" aria-hidden="true">
          <circle cx="17" cy="17" r="17" fill="var(--icon-fill)"/>
          <circle cx="17" cy="17" r="8.5" fill="var(--icon-glyph)"/>
          <g fill="none" stroke="var(--icon-fill)" stroke-width="1.1">
            <ellipse cx="17" cy="17" rx="3.8" ry="8.5"/>
            <line x1="17" y1="8.5" x2="17" y2="25.5"/>
            <line x1="8.5" y1="17" x2="25.5" y2="17"/>
            <line x1="10" y1="12.8" x2="24" y2="12.8"/>
            <line x1="10" y1="21.2" x2="24" y2="21.2"/>
          </g>
        </svg>
        <span class="contact__text">www.lumirabeauty.com.au</span>
      </div>
    </div>
  </section>

</main>
</body>
</html>
```